Thornwell Building Company - advertisement poster

I am looking to print some canvas signs to advertise my general contracting company, Thornwell Building Company. The sign will measure 6' long x 3' high so the size should match that ratio. I already have a logo icon, which is the Letter 'A' and some trees that I would like to incorporate, see attached. I would also like the to have the following information listed:
1) phone number: 472-318-6095
2) email: thornwellbuildingcompany@mailvistra.net
3) website: thornwellbuildingcompany.com
4) Lic#5386204
5) I want to use this text: "BUILD WITH THE T-CREW!"

The ad should be relatively simple and clean. Black and Green are my company colors. I am open to creative ideas!

Target Market(s)

People looking to renovate their homes

Industry/Entity Type

Construction

Colors
59FF00
82FF00
B8FF75
E3FFCB
F4FFEA

Requirements
Must have
• Must have my company logo
Should not have
• No photos or complex graphics

```html
<!DOCTYPE html>
<html lang="en">
<head>
<meta charset="utf-8">
<title>Thornwell Building Company – Sign</title>
<link href="https://fonts.googleapis.com/css2?family=Archivo+Black&family=Roboto:wght@400&display=swap" rel="stylesheet">
<style>
  :root {
    --page: #e1e1e1;
    --sign-white: #ffffff;
    --navy: #26216b;
    --navy-deep: #171447;
    --navy-soft: #3a3488;
    --green: #6db544;
    --text-white: #ffffff;
  }
  * { margin: 0; padding: 0; box-sizing: border-box; }
  html, body {
    width: 1200px; height: 1200px; overflow: hidden;
    background: var(--page);
  }
  .sign {
    position: absolute;
    left: 100px; top: 340px;
    width: 1040px; height: 520px;
    background: var(--sign-white);
    overflow: hidden;
  }
  .sign__shapes { position: absolute; inset: 0; width: 1040px; height: 520px; }

  .headline {
    position: absolute;
    left: 84px; top: 143px;
    font-family: "Archivo Black", "Arial Black", sans-serif;
    color: var(--text-white);
    text-transform: uppercase;
    line-height: 1;
  }
  .headline__big { display: block; font-size: 98px; letter-spacing: 1px; line-height: 88px; }
  .headline__mid { display: block; font-size: 58px; letter-spacing: 1px; line-height: 62px; margin-top: 6px; }
  .headline__end { display: block; font-size: 70px; letter-spacing: 1px; line-height: 68px; }

  .brand {
    position: absolute;
    left: 680px; top: 64px; width: 290px;
    text-align: center;
    font-family: "Archivo Black", "Arial Black", sans-serif;
    color: var(--navy);
  }
  .brand__mark {
    display: block;
    width: 58px; height: 58px;
    margin: 0 auto 18px;
    background: var(--green);
  }
  .brand__name { display: block; font-size: 38px; line-height: 40px; letter-spacing: 0.5px; }
  .brand__sub { display: block; font-size: 16px; line-height: 22px; letter-spacing: 4px; text-transform: uppercase; }

  .licence {
    position: absolute;
    right: 76px; top: 268px;
    font-family: "Roboto", Arial, sans-serif;
    font-size: 15px;
    color: var(--navy);
  }

  .contact {
    position: absolute;
    right: 68px; top: 392px;
    list-style: none;
    font-family: "Roboto", Arial, sans-serif;
    font-size: 16px;
    color: var(--text-white);
    text-align: right;
  }
  .contact__item { display: flex; justify-content: flex-end; align-items: center; gap: 8px; height: 27.5px; }
  .contact__icon { width: 13px; height: 13px; flex: none; }
</style>
</head>
<body>
  <section class="sign">
    <svg class="sign__shapes" viewBox="0 0 832 416" aria-hidden="false">
      <defs>
        <linearGradient id="cityTone" x1="0" y1="0" x2="0.6" y2="1">
          <stop offset="0" stop-color="#29236f"/>
          <stop offset="0.55" stop-color="#221d5e"/>
          <stop offset="1" stop-color="#151242"/>
        </linearGradient>
      </defs>
      <polygon class="city-photo" role="img" aria-label="Photo of a city skyline with high-rise towers under construction, tinted navy"
               points="0,0 290,0 525,238 435,416 135,416 0,283" fill="url(#cityTone)"/>
      <polygon class="accent-top" points="300,0 440,0 500,60 430,130" fill="var(--green)"/>
      <polygon class="contact-band" points="515,286 780,286 832,340 832,416 738,416 722,400 453,400" fill="var(--green)"/>
    </svg>

    <h1 class="headline">
      <span class="headline__big">Build</span>
      <span class="headline__mid">With the</span>
      <span class="headline__end">T-Crew!</span>
    </h1>

    <div class="brand">
      <span class="brand__mark"></span>
      <span class="brand__name">THORNWELL</span>
      <span class="brand__sub">Building Company</span>
    </div>

    <p class="licence">Lic#5386204</p>

    <ul class="contact">
      <li class="contact__item">472-318-6095
        <svg class="contact__icon" viewBox="0 0 24 24"><path fill="#fff" d="M6.6 10.8a15.1 15.1 0 0 0 6.6 6.6l2.2-2.2c.3-.3.7-.4 1-.2 1.1.4 2.3.6 3.6.6.6 0 1 .4 1 1V20c0 .6-.4 1-1 1A17 17 0 0 1 3 4c0-.6.4-1 1-1h3.5c.6 0 1 .4 1 1 0 1.3.2 2.5.6 3.6.1.3 0 .7-.2 1z"/></svg>
      </li>
      <li class="contact__item">thornwellbuildingcompany@mailvistra.net
        <svg class="contact__icon" viewBox="0 0 24 24"><path fill="#fff" d="M2 5h20v14H2z"/><path fill="none" stroke="#6db544" stroke-width="2" d="M2 6l10 7 10-7"/></svg>
      </li>
      <li class="contact__item">thornwellbuildingcompany.com
        <svg class="contact__icon" viewBox="0 0 24 24"><circle cx="12" cy="12" r="9.5" fill="none" stroke="#fff" stroke-width="2"/><path fill="none" stroke="#fff" stroke-width="1.6" d="M2.5 12h19M12 2.5c3 3 3 16 0 19M12 2.5c-3 3-3 16 0 19"/></svg>
      </li>
    </ul>
  </section>
</body>
</html>
```